Design/Build Engineering and Detailing Service 3D Modeling

We are an engineering company in the construction industry. We specialize in designing blueprints for new construction projects such as high rise buildings, hospitals, hotels, public schools, large scale apartment buildings etc.

We want to have a clean, modern, cutting edge design, but it should be clear and easy to navigate. Related videos in the background of the page are a plus. For example The page now has a picture of the marlow crest span in san francisco with fog rolling over it and cars driving on the bridge, saying website coming soon. This is played at a faster frame rate. We want to have customer portal to access files, fill out work orders, pay invoices, make suggestions etc.
Updates

Target Market(s)

Los Angeles, San francisco, San Jose, Portland, Seattle, Las Vegas, Denver

Industry/Entity Type

Construction

Coding

Coded - Design and coding required

Number of Pages Required

4 page

Font styles to use
Serif
Sans Serif

Colors
3276b5
0255a3
85acd3
9d9d9d
5c5c5c
ec1f27
000000
fbee3f
00a990

Requirements
Must have
• Work Examples, mission statement, team members, capabilities. Convey the technical aspects of the business in a way that someone can understand the companies capabilities without knowing the technical side of the business.
Nice to have
• Construction related Videos, Downtown city center skylines, clean, modern, concise design.
Should not have
• Overly complex navigation. should not be to busy

```html
<!DOCTYPE html>
<html lang="en">
<head>
<meta charset="utf-8">
<title>Ardent Grid Engineering</title>
<link href="https://fonts.googleapis.com/css2?family=Roboto:wght@300;400;500;700;900&family=Roboto+Condensed:wght@700&display=swap" rel="stylesheet">
<style>
:root{
  --blue:#1396dc;
  --blue-dark:#0b7fbf;
  --ink:#2d2d2d;
  --text:#5c5c5c;
  --muted:#9d9d9d;
  --topbar:#4d4d4d;
  --footer:#474747;
  --footer-bottom:#3a3a3a;
  --concrete:#e4e4e2;
  --white:#ffffff;
  --black:#000000;
  --red:#ec1f27;
}
*{margin:0;padding:0;box-sizing:border-box}
html,body{width:1200px;height:3618px;overflow:hidden;background:var(--white)}
body{font-family:"Roboto",Arial,sans-serif;color:var(--text);position:relative}
.abs{position:absolute}
.btn{position:absolute;display:flex;align-items:center;justify-content:center;font-size:15px;color:var(--white);background:var(--blue)}
.center{left:0;width:1200px;text-align:center}

/* top bar */
.topbar{position:absolute;top:0;left:0;width:1200px;height:30px;background:var(--topbar)}
.topbar .phone{position:absolute;right:90px;top:6px;color:var(--white);font-size:17px;display:flex;align-items:center;gap:8px}

/* nav */
.site-header{position:absolute;top:30px;left:0;width:1200px;height:60px;background:var(--white)}
.brand{position:absolute;left:172px;top:15px;display:flex;align-items:center;gap:8px;font-size:24px;color:var(--ink);font-weight:400}
.brand .mark{width:30px;height:30px;background:var(--blue)}
.main-nav{position:absolute;right:170px;top:22px;display:flex;gap:36px;font-size:14px;color:var(--muted)}
.main-nav .active{color:var(--blue)}

/* hero */
.hero{position:absolute;top:90px;left:0;width:1200px;height:558px;background:linear-gradient(180deg,#3d4a57 0%,#8a7866 38%,#e18a3a 62%,#3c2e2a 80%,#1c1a1c 100%)}
.hero h1{position:absolute;top:192px;font-family:"Roboto Condensed",Arial,sans-serif;font-size:39px;color:var(--white);letter-spacing:.5px}
.hero .lead{position:absolute;top:254px;font-size:21px;color:var(--white)}
.hero .btn{left:478px;top:318px;width:244px;height:50px;font-size:18px}

/* welcome */
.welcome .eyebrow{top:724px;font-size:18px;color:var(--ink);font-weight:300}
.welcome h2{top:744px;font-size:28px;color:var(--blue);font-weight:700}
.welcome .rule{left:555px;top:788px;width:90px;height:1px;background:#cfcfcf}
.welcome p{top:806px;left:370px;width:460px;text-align:center;font-size:14px;line-height:22px}

/* services */
.services{position:absolute;top:905px;left:0;width:1200px;height:443px;background:radial-gradient(ellipse at 40% 50%,#eeeeec 0%,var(--concrete) 60%,#d6d6d4 100%)}
.services h3{top:62px;font-size:17px;color:var(--blue);font-weight:400}
.services .rule{left:555px;top:86px;width:90px;height:1px;background:#c4c4c4}
.service{position:absolute;width:290px;display:flex;gap:12px}
.service .icon{width:50px;height:50px;flex:none}
.service h4{font-size:16px;font-weight:500;color:var(--ink);margin-top:2px}
.service p{font-size:12.5px;line-height:17px;color:var(--text);margin-top:3px}
.services .btn{left:528px;top:355px;width:166px;height:42px;background:var(--black);font-size:14px}

/* about */
.about h3{left:172px;top:1513px;font-size:17px;color:var(--blue);font-weight:400}
.about .rule{left:172px;top:1540px;width:120px;height:1px;background:#d0d0d0}
.about p{left:172px;top:1560px;width:440px;font-size:13.5px;line-height:21px}
.about .btn{left:172px;top:1664px;width:166px;height:42px;font-size:14px}
.device{left:724px;top:1387px;width:300px;height:482px;border-radius:30px 30px 0 0;background:linear-gradient(180deg,#222 0%,#222 6%,#b98a58 14%,#d8b07c 40%,#6e88a8 70%,#2a2a2a 100%)}

/* leadership */
.leader{position:absolute;top:1869px;left:0;width:1200px;height:453px;background:linear-gradient(90deg,#1e1e1e 0%,#3a3a3a 45%,#5a5753 75%,#2c2c2c 100%)}
.leader .portrait{left:530px;top:49px;width:140px;height:140px;border-radius:50%;border:4px solid var(--white);background:radial-gradient(circle at 50% 40%,#d2a888 0%,#8a6a55 55%,#3d3d3d 100%)}
.leader h4{top:203px;font-size:17px;color:var(--white);font-weight:700}
.leader .role{top:229px;font-size:12px;color:#d8d8d8}
.leader p{left:270px;top:262px;width:660px;text-align:center;font-size:13.5px;line-height:20px;color:#ececec}
.leader .btn{left:534px;top:362px;width:153px;height:38px;font-size:14px}

/* team */
.team{position:absolute;top:2322px;left:0;width:1200px;height:503px;background:var(--blue)}
.team h3{top:56px;font-size:19px;color:var(--white);font-weight:400}
.team .rule{left:560px;top:84px;width:80px;height:1px;background:rgba(255,255,255,.7)}
.member{position:absolute;top:141px;width:211px;height:317px;background:var(--white)}
.member .photo{height:215px}
.member h5{margin-top:14px;text-align:center;font-size:13px;color:var(--ink);font-weight:500}
.member p{margin:4px auto 0;width:170px;text-align:center;font-size:11.5px;line-height:15px;color:var(--muted)}
.member .social{display:flex;justify-content:center;gap:6px;margin-top:8px}
.member .social span{width:20px;height:20px;border-radius:50%}

/* projects */
.projects h3{top:2873px;font-size:19px;color:var(--ink);font-weight:400}
.projects .rule{left:555px;top:2902px;width:90px;height:1px;background:#d0d0d0}
.strip{position:absolute;top:2955px;height:241px}
.strip.plan{background:linear-gradient(135deg,#f7f7f7 0%,#e2e2e2 50%,#f2f2f2 100%)}
.strip.focus{background:#2a2a2a;display:flex;align-items:center;justify-content:center;flex-direction:column;color:var(--white);font-size:17px;gap:6px}
.arrow{position:absolute;top:3060px;font-size:22px;color:var(--ink)}

/* footer */
.site-footer{position:absolute;top:3241px;left:0;width:1200px;height:377px;background:var(--footer);color:#dcdcdc}
.site-footer h4{position:absolute;font-size:16px;color:var(--white);font-weight:500}
.site-footer .col{position:absolute;font-size:13px;line-height:18px}
.contact-line{display:flex;gap:12px;margin-bottom:14px;align-items:flex-start}
.contact-line i{width:22px;height:22px;border-radius:50%;background:var(--blue);flex:none;display:flex;align-items:center;justify-content:center}
.news-item{margin-bottom:16px}
.news-item small{display:block;color:var(--blue);font-size:11px}
.subscribe{position:absolute;left:727px;top:3497px;width:300px;height:34px;background:var(--white);display:flex;align-items:center;justify-content:space-between;padding-left:12px;font-size:12px;color:var(--muted)}
.subscribe span.go{width:44px;height:34px;background:var(--white);display:flex;align-items:center;justify-content:center}
.footer-bar{position:absolute;top:3573px;left:0;width:1200px;height:45px;background:var(--footer-bottom);font-size:12px;color:#cfcfcf}
.footer-nav{position:absolute;left:172px;top:15px;display:flex;gap:24px}
.footer-nav .active{color:var(--blue)}
.copyright{position:absolute;right:172px;top:15px}
</style>
</head>
<body>

<div class="topbar">
  <div class="phone">
    <svg width="16" height="16" viewBox="0 0 24 24"><circle cx="12" cy="12" r="11" fill="#fff"/><path d="M8 6l2 3-1.4 1.4a9 9 0 005 5L15 14l3 2-1.5 2.3C11 18 6 13 5.7 7.5z" fill="#4d4d4d"/></svg>
    702.555.0148
  </div>
</div>

<header class="site-header">
  <div class="brand"><span class="mark"></span>Ardent Grid Engineering</div>
  <nav class="main-nav">
    <span class="active">Home</span><span>Mission Statement</span><span>Projects</span><span>Team</span><span>Contact Us</span>
  </nav>
</header>

<section class="hero" role="img" aria-label="Marlow Crest Span suspension bridge over a city skyline at sunset">
  <h1 class="center">WE ARE A FULL SERVICE ENGINEERING</h1>
  <p class="lead center">and specializes in complete plumbing coordination and design</p>
  <span class="btn">REQUEST A QOUTE</span>
</section>

<section class="welcome">
  <p class="abs center eyebrow">WELCOME TO</p>
  <h2 class="abs center">Ardent Grid Engineering</h2>
  <span class="abs rule"></span>
  <p class="abs">We are a full service engineering and detailing firm that specializes in complete plumbing coordination and design services</p>
</section>

<section class="services">
  <h3 class="abs center">WHAT WE DO</h3>
  <span class="abs rule"></span>

  <div class="service" style="left:172px;top:118px">
    <svg class="icon" viewBox="0 0 50 50"><rect width="50" height="50" fill="var(--blue)"/><path d="M13 22l12-7 12 7-12 7z M18 26v7h14v-7" fill="none" stroke="#fff" stroke-width="2.5"/></svg>
    <div><h4>Design/Build Projects</h4><p>Lorem ipsum dolor sit amet, consectetuer adipiscing elit, sed diam</p></div>
  </div>
  <div class="service" style="left:473px;top:118px">
    <svg class="icon" viewBox="0 0 50 50"><rect width="50" height="50" fill="var(--blue)"/><rect x="13" y="14" width="24" height="22" fill="none" stroke="#fff" stroke-width="2.5"/><path d="M13 21h24M20 14v22" stroke="#fff" stroke-width="2"/></svg>
    <div><h4>Plan/Spec Projects</h4><p>Ut wisi enim ad minim veniam, quis nostrud exerci tation ullamcorper</p></div>
  </div>
  <div class="service" style="left:766px;top:118px">
    <svg class="icon" viewBox="0 0 50 50"><rect width="50" height="50" fill="var(--blue)"/><path d="M14 36L36 14M14 36h10M14 36V26" stroke="#fff" stroke-width="2.5" fill="none"/></svg>
    <div><h4>Vantor Layout</h4><p>Duis autem vel eum iriure dolor in hendrerit in vulputate velit esse</p></div>
  </div>
  <div class="service" style="left:172px;top:230px">
    <svg class="icon" viewBox="0 0 50 50"><rect width="50" height="50" fill="var(--blue)"/><circle cx="17" cy="17" r="4" fill="#fff"/><circle cx="33" cy="25" r="4" fill="#fff"/><circle cx="19" cy="34" r="4" fill="#fff"/><path d="M17 17L33 25L19 34" stroke="#fff" stroke-width="2" fill="none"/></svg>
    <div><h4>Spool sheets for fabrication</h4><p>vel illum dolore eu feugiat nulla facilisis at vero eros et accumsan</p></div>
  </div>
  <div class="service" style="left:473px;top:230px">
    <svg class="icon" viewBox="0 0 50 50"><rect width="50" height="50" fill="var(--blue)"/><path d="M14 36V22l11-8 11 8v14" fill="none" stroke="#fff" stroke-width="2.5"/><path d="M21 36v-8h8v8" stroke="#fff" stroke-width="2" fill="none"/></svg>
    <div><h4>Spool maps for fabrication</h4><p>dignissim qui blandit praesent luptatum zzril delenit augue duis</p></div>
  </div>
  <div class="service" style="left:766px;top:230px">
    <svg class="icon" viewBox="0 0 50 50"><rect width="50" height="50" fill="var(--blue)"/><rect x="12" y="18" width="26" height="14" fill="none" stroke="#fff" stroke-width="2.5"/><path d="M17 18v14M25 18v14M33 18v14" stroke="#fff" stroke-width="2"/></svg>
    <div><h4>Plumbing engineering</h4><p>Typi non habent claritatem insitam; est usus legentis in iis qui facit eorum</p></div>
  </div>

  <span class="btn">View All Services</span>
</section>

<section class="about">
  <h3 class="abs">WHO WE ARE</h3>
  <span class="abs rule"></span>
  <p class="abs">Claritas est etiam processus dynamicus, qui sequitur mutationem consuetudium lectorum. Mirum est notare quam littera gothica, quam nunc putamus parum claram, anteposuerit litterarum formas humanitatis per seacula quarta decima et quinta decima</p>
  <span class="btn">Watch The Video</span>
  <div class="abs device" role="img" aria-label="Smartphone playing a video of construction workers on a timber frame"></div>
</section>

<section class="leader">
  <div class="abs portrait" role="img" aria-label="Portrait of the chief executive"></div>
  <h4 class="abs center">OWEN HARTLEY</h4>
  <p class="abs center role">CEO | FOUNDER</p>
  <p class="abs">Owen's responsibilities are to manage company personnel, coordinate BIM efforts, detailing and shop drawings for traditional and IPD projects. These responsibilities all culminate into delivering a constructible, efficient, and cost effective design that distributes savings to the owner over the life span of the building or facility.</p>
  <span class="btn">More About CEO</span>
</section>

<section class="team">
  <h3 class="abs center">OUR TEAM</h3>
  <span class="abs rule"></span>

  <div class="member" style="left:172px">
    <div class="photo" role="img" aria-label="Team member in business suit" style="background:linear-gradient(180deg,#cfd6da,#7a8590)"></div>
    <h5>LOREM IPSUM DOLOR</h5>
    <p>consectetuer adipiscing elit, sed diam nonummy</p>
    <div class="social"><span style="background:var(--blue-dark)"></span><span style="background:var(--red)"></span><span style="background:#c9302c"></span></div>
  </div>
  <div class="member" style="left:389px">
    <div class="photo" role="img" aria-label="Team member in hard hat at work" style="background:linear-gradient(180deg,#8a9bb0,#7a4a3a)"></div>
    <h5>LOREM IPSUM DOLOR</h5>
    <p>consectetuer adipiscing elit, sed diam nonummy</p>
    <div class="social"><span style="background:var(--blue-dark)"></span><span style="background:var(--red)"></span><span style="background:#c9302c"></span></div>
  </div>
  <div class="member" style="left:603px">
    <div class="photo" role="img" aria-label="Smiling team member" style="background:linear-gradient(180deg,#dfe5e8,#9aa6ae)"></div>
    <h5>LOREM IPSUM DOLOR</h5>
    <p>consectetuer adipiscing elit, sed diam nonummy</p>
    <div class="social"><span style="background:var(--blue-dark)"></span><span style="background:var(--red)"></span><span style="background:#c9302c"></span></div>
  </div>
  <div class="member" style="left:820px">
    <div class="photo" role="img" aria-label="Team member wearing a white hard hat" style="background:linear-gradient(180deg,#f2f2f2,#d4a77e)"></div>
    <h5>LOREM IPSUM DOLOR</h5>
    <p>consectetuer adipiscing elit, sed diam nonummy</p>
    <div class="social"><span style="background:var(--blue-dark)"></span><span style="background:var(--red)"></span><span style="background:#c9302c"></span></div>
  </div>
</section>

<section class="projects">
  <h3 class="abs center">OUR PROJECTS</h3>
  <span class="abs rule"></span>
  <div class="strip plan" style="left:0;width:300px" role="img" aria-label="Floor plan drawing"></div>
  <div class="strip focus" style="left:300px;width:300px">
    <svg width="22" height="22" viewBox="0 0 24 24"><circle cx="10" cy="10" r="6" fill="none" stroke="#fff" stroke-width="2"/><path d="M15 15l6 6" stroke="#fff" stroke-width="2"/></svg>
    Lorem ipsum
  </div>
  <div class="strip plan" style="left:600px;width:300px" role="img" aria-label="Building section drawing"></div>
  <div class="strip plan" style="left:900px;width:300px" role="img" aria-label="Piping layout drawing"></div>
  <span class="arrow" style="left:18px">&#8249;</span>
  <span class="arrow" style="right:18px">&#8250;</span>
</section>

<footer class="site-footer">
  <h4 style="left:172px;top:52px">Ardent Grid Engineering</h4>
  <div class="col" style="left:172px;top:82px;width:250px">
    <p>Lorem ipsum dolor sit amet, consectetuer adipiscing elit, sed diam nonummy nibh euismod tincidunt ut laoreet dolore magna aliquam erat volutpat</p>
    <div style="margin-top:18px">
      <div class="contact-line"><i><svg width="11" height="11" viewBox="0 0 24 24"><path d="M6 3l4 5-2 2a12 12 0 006 6l2-2 5 4-2 3C10 21 3 14 3 5z" fill="#fff"/></svg></i>702.555.0148</div>
      <div class="contact-line"><i><svg width="11" height="11" viewBox="0 0 24 24"><rect x="3" y="6" width="18" height="12" fill="none" stroke="#fff" stroke-width="2"/><path d="M3 6l9 7 9-7" fill="none" stroke="#fff" stroke-width="2"/></svg></i>Lorem ipsum@dolor sit amet</div>
      <div class="contact-line"><i><svg width="11" height="11" viewBox="0 0 24 24"><path d="M12 2a7 7 0 00-7 7c0 5 7 13 7 13s7-8 7-13a7 7 0 00-7-7z" fill="#fff"/></svg></i><span>123,sed diam nonummy nibh euismod<br>tincidunt ut</span></div>
    </div>
  </div>

  <h4 style="left:490px;top:52px">Latest News</h4>
  <div class="col" style="left:490px;top:82px;width:170px">
    <div class="news-item">Lorem ipsum dolor sit amet, consectetuer<small>14 June 2016</small></div>
    <div class="news-item">Lorem ipsum dolor sit amet, consectetuer<small>14 June 2016</small></div>
    <div class="news-item">Lorem ipsum dolor sit amet, consectetuer<small>14 June 2016</small></div>
    <div class="news-item">Lorem ipsum dolor sit amet, consectetuer<small>14 June 2016</small></div>
  </div>

  <h4 style="left:727px;top:48px;font-size:18px">Lorem ipsum</h4>
  <div class="col" style="left:727px;top:76px;width:300px">Lorem ipsum dolor sit amet, consectetuer adipiscing elit, sed diam nonummy nibh euismod tincidunt ut laoreet dolore magna aliquam erat volutpat</div>
  <h4 style="left:727px;top:222px;font-size:18px">Email Subscription</h4>
</footer>
<div class="subscribe">Email Address<span class="go"><svg width="22" height="16" viewBox="0 0 24 18"><rect x="1" y="1" width="22" height="16" fill="var(--black)"/><path d="M1 1l11 9 11-9" fill="none" stroke="#fff" stroke-width="1.5"/></svg></span></div>

<div class="footer-bar">
  <nav class="footer-nav"><span class="active">Home</span><span>Mission Statement</span><span>Projects</span><span>Team</span><span>Contact Us</span></nav>
  <p class="copyright">All contents © 2016 ArdentGrid. All rights reserved</p>
</div>

</body>
</html>
```